Occupational Therapy Needs an eye catching brochure for new business

I need a brochure for a new business that would be eye catching. I am an occupational therapist and this business will specifically deal with auditory processing delays and visual processing delays.If the childs delays stem from unintegrated reflexes that will be dealt with,as well. I have attached a brochure that I created. After having created it I decided that I wanted to seek professional graphics artist to help create an eye catching brochure that would attract more attention then my current unprofessional one. The attached brochures backgrounds should be changed. The wording should be changed and be more professionalized but the message should stay. I do not have a logo, since I am new, so you can create one for me, as well.
Updates

Please keep it a tri-fold. I have added the original brother file .edit and a word document with my text inside. Please give the brochure a professional look. I want those seeing my brochure to get the feel that my therapy business is a very professional and experienced business.Thank You Added Sunday, April 26, 2015

Target Market(s)

Parents of children with learning delays, whom are struggling and not getting good grades in school.

Industry/Entity Type

Business

Requirements
Must have
• Please keep it a tri-fold brochure
Nice to have
• Please include on the front page the following questions, they can be worded differently:
• Does your child have difficulty learning ABC and /or aleph bet?
• Does your child know the information for the test and does not do well on the test?
• Does your child have difficulty remembering name and dates in school, for test, or every day life?
Should not have
• Please do not include pictures of Adults in the brochure.

```html
<!DOCTYPE html>
<html lang="en">
<head>
<meta charset="utf-8">
<title>Help Your Child Flourish – Brochure Cover</title>
<link rel="stylesheet" href="https://fonts.googleapis.com/css2?family=Jost:wght@300;400&display=swap">
<style>
  :root {
    --page-bg: #efe9e1;
    --paper: #ffffff;
    --ink-light: #ffffff;
    --brand-ink: #6b5f8e;
    --tone-blue: #4f7fa8;
    --tone-teal: #6db5a8;
    --tone-yellow: #f2bd3c;
    --tone-orange: #f1982f;
    --tone-green: #93bb4c;
    --tone-plum: #6b5f8e;
  }
  * { box-sizing: border-box; margin: 0; padding: 0; }
  html, body {
    width: 1133px;
    height: 1200px;
    overflow: hidden;
    background: var(--page-bg);
  }
  .cover-panel {
    position: absolute;
    left: 321px;
    top: 30px;
    width: 490px;
    height: 1140px;
    background: var(--paper);
    box-shadow: 0 6px 22px rgba(0, 0, 0, 0.12);
    font-family: "Jost", "Futura", sans-serif;
  }
  .cover-art {
    position: absolute;
    inset: 0;
  }
  .cover-copy {
    position: absolute;
    left: 40px;
    right: 30px;
    top: 110px;
    color: var(--ink-light);
    text-align: center;
  }
  .cover-title {
    font-weight: 300;
    font-size: 86px;
    line-height: 0.98;
    letter-spacing: 1px;
    text-transform: uppercase;
  }
  .cover-questions {
    margin-top: 62px;
    font-weight: 300;
    font-size: 18px;
    line-height: 1.4;
  }
  .cover-divider {
    display: block;
    width: 8px;
    height: 8px;
    margin: 18px auto;
    border-radius: 50%;
    background: var(--ink-light);
  }
  .cover-statement {
    font-weight: 300;
    font-size: 18px;
    line-height: 1.4;
  }
  .brand-name {
    position: absolute;
    left: 0;
    right: 0;
    bottom: 62px;
    display: flex;
    align-items: center;
    justify-content: center;
    gap: 12px;
    font-weight: 400;
    font-size: 20px;
    letter-spacing: 4px;
    text-transform: uppercase;
    color: var(--brand-ink);
  }
  .brand-dot {
    width: 12px;
    height: 12px;
    border-radius: 50%;
    background: var(--brand-ink);
  }
</style>
</head>
<body>
  <section class="cover-panel">
    <svg class="cover-art" width="490" height="1140" viewBox="0 0 490 1140" role="img"
         aria-label="Flowing overlapping translucent ribbons in blue, teal, yellow, orange, green and plum with a fine dot texture">
      <defs>
        <linearGradient id="ribbonTones" x1="0" y1="0" x2="1" y2="0">
          <stop offset="0" stop-color="var(--tone-blue)"/>
          <stop offset="0.18" stop-color="var(--tone-teal)"/>
          <stop offset="0.38" stop-color="var(--tone-yellow)"/>
          <stop offset="0.52" stop-color="var(--tone-orange)"/>
          <stop offset="0.68" stop-color="var(--tone-yellow)"/>
          <stop offset="0.84" stop-color="var(--tone-green)"/>
          <stop offset="1" stop-color="var(--tone-plum)"/>
        </linearGradient>
      </defs>
      <path d="M70 30 H360 Q390 30 400 55 Q412 85 460 85 V960
               Q380 1000 250 985 Q130 970 70 1000 Q38 1015 38 975 V62 Q38 30 70 30 Z"
            fill="url(#ribbonTones)"/>
    </svg>

    <div class="cover-copy">
      <h1 class="cover-title">Help<br>Your<br>Child<br>Flourish</h1>
      <p class="cover-questions">
        Your child has difficulty learning ABC?<br>
        Knows all the information but fails the test?<br>
        Has difficulty remembering names and dates?
      </p>
      <span class="cover-divider"></span>
      <p class="cover-statement">Schools require great auditory<br>and visual processing skills</p>
      <span class="cover-divider"></span>
      <p class="cover-statement">We can help your child improve his.</p>
    </div>

    <p class="brand-name"><span class="brand-dot"></span>Bright Path Therapy</p>
  </section>
</body>
</html>
```